Stationary For Engineering & Consultancy Company
Harbourline Sound Consulting Inc.
Stationary For Engineering & Consultancy Company - Consulting
Professional
Rajveer Talwani
President (MSc. Applied tremolo)
42 Willowmere Crt, Brampton, Ontario L6R 3J8
info@harbourlinesound.example
www.harbourlinesound.example

```html
<!DOCTYPE html>
<html lang="en">
<head>
<meta charset="utf-8">
<title>Harbourline Sound Consulting Inc. – Business Card</title>
<link rel="stylesheet" href="https://fonts.googleapis.com/css2?family=Open+Sans:wght@400;600&display=swap">
<style>
  :root {
    --page-bg: #e9e9e6;
    --card-face: #f4f5f2;
    --card-shade: #dfe2dc;
    --brand-green: #4c8a1c;
    --green-light: #5d9a24;
    --green-dark: #173608;
    --swoosh-grey: #5a5d5a;
    --swoosh-light: #b9bcb8;
    --text-light: #ffffff;
    --text-soft: #dbe8cf;
    --text-muted: #7a7f78;
  }
  * { box-sizing: border-box; margin: 0; padding: 0; }
  html, body {
    width: 1200px; height: 768px; overflow: hidden;
    background: var(--page-bg);
    font-family: "Open Sans", Arial, sans-serif;
  }
  .business-card {
    position: absolute; left: 100px; top: 99px;
    width: 1000px; height: 570px;
    background: linear-gradient(135deg, var(--card-face) 0%, var(--card-shade) 100%);
    border-radius: 10px; overflow: hidden;
    box-shadow: 0 12px 34px rgba(0,0,0,0.18);
  }
  .card-panel { position: absolute; inset: 0; width: 1000px; height: 570px; }
  .brand-block {
    position: absolute; left: 40px; top: 150px; width: 420px;
    text-align: center;
  }
  .brand-mark {
    width: 70px; height: 70px; margin: 0 auto 26px;
    background: var(--brand-green);
  }
  .brand-name {
    font-weight: 600; font-size: 34px; line-height: 1.2;
    color: var(--brand-green);
  }
  .brand-tagline {
    margin-top: 12px; font-size: 12px; letter-spacing: 3px;
    text-transform: uppercase; color: var(--text-muted);
  }
  .contact-block {
    position: absolute; left: 640px; top: 112px; width: 330px;
    color: var(--text-light);
  }
  .person-name { font-size: 24px; font-weight: 600; }
  .person-role { font-size: 16px; color: var(--text-soft); margin-top: 2px; }
  .address { margin-top: 58px; font-size: 16px; line-height: 1.5; color: var(--text-light); }
  .contact-list { list-style: none; margin-top: 36px; }
  .contact-list li {
    display: flex; align-items: center; gap: 12px;
    font-size: 15px; line-height: 29px; color: var(--text-light);
  }
  .contact-list svg { width: 15px; height: 15px; flex: none; }
</style>
</head>
<body>
<article class="business-card">
  <svg class="card-panel" viewBox="0 0 1000 570" aria-hidden="true">
    <defs>
      <radialGradient id="panelGreen" cx="0.25" cy="0.45" r="0.9">
        <stop offset="0" stop-color="var(--green-light)"/>
        <stop offset="0.55" stop-color="#2f6212"/>
        <stop offset="1" stop-color="var(--green-dark)"/>
      </radialGradient>
      <linearGradient id="swooshGrey" x1="0" y1="0" x2="0" y2="1">
        <stop offset="0" stop-color="var(--swoosh-light)"/>
        <stop offset="0.5" stop-color="var(--swoosh-grey)"/>
        <stop offset="1" stop-color="var(--swoosh-light)"/>
      </linearGradient>
    </defs>
    <path d="M548 0 C470 150 462 400 510 570 L1000 570 L1000 0 Z" fill="url(#swooshGrey)"/>
    <path d="M575 0 C500 150 492 400 535 570 L1000 570 L1000 0 Z" fill="url(#panelGreen)"/>
  </svg>

  <div class="brand-block">
    <div class="brand-mark"></div>
    <p class="brand-name">Harbourline Sound<br>Consulting Inc.</p>
    <p class="brand-tagline">Engineering &amp; Consulting Services</p>
  </div>

  <div class="contact-block">
    <h1 class="person-name">Rajveer Talwani</h1>
    <p class="person-role">consultant</p>
    <p class="address">42 Willowmere Crt, Brampton,<br>Ontario L6R 3J8</p>
    <ul class="contact-list">
      <li><svg viewBox="0 0 16 16"><path fill="#fff" d="M3 1h3l1.5 4-2 1.2a8 8 0 0 0 4.3 4.3L11 8.5l4 1.5v3a2 2 0 0 1-2 2A12 12 0 0 1 1 3a2 2 0 0 1 2-2z"/></svg>905 555 0142</li>
      <li><svg viewBox="0 0 16 16"><rect x="4" y="1" width="8" height="14" rx="1.5" fill="none" stroke="#fff" stroke-width="1.6"/><circle cx="8" cy="12.3" r="0.9" fill="#fff"/></svg>905 555 0178</li>
      <li><svg viewBox="0 0 16 16"><rect x="4" y="1" width="8" height="5" fill="#fff"/><rect x="1" y="6" width="14" height="6" rx="1" fill="#fff"/><rect x="4" y="10" width="8" height="5" fill="#fff" stroke="#2f6212"/></svg>905 555 0193</li>
      <li><svg viewBox="0 0 16 16"><rect x="1" y="3" width="14" height="10" rx="1" fill="#fff"/><path d="M1.5 3.5 8 9l6.5-5.5" fill="none" stroke="#2f6212" stroke-width="1.3"/></svg>info@harbourlinesound.example</li>
      <li><svg viewBox="0 0 16 16"><circle cx="8" cy="8" r="6.5" fill="none" stroke="#fff" stroke-width="1.4"/><ellipse cx="8" cy="8" rx="2.7" ry="6.5" fill="none" stroke="#fff" stroke-width="1.2"/><path d="M1.5 8h13" stroke="#fff" stroke-width="1.2"/></svg>www.harbourlinesound.example</li>
    </ul>
  </div>
</article>
</body>
</html>
```